Open Every Door Sports Career Conference

Open Every Door is a first-time in-person event focused on helping people of color learn about and obtain jobs and/or internships in the business of Sports. We are looking for a Power Point deck that we can use to assist in selling sponsorships in addition to providing general awareness. All of the details are included on the attached PP that was created in-house. I am looking for something more modern and up-to-date. This looks very dated and simplistic. The photos and graphics really need to focus on students of color and not white people.

```html
<!DOCTYPE html>
<html lang="en">
<head>
<meta charset="utf-8">
<title>Open Every Door Sports Career Conference</title>
<link href="https://fonts.googleapis.com/css2?family=Poppins:wght@400;500;700;800&family=Kalam:wght@400&display=swap" rel="stylesheet">
<style>
  :root{
    --navy:#2a3591;
    --orange:#f26b1d;
    --ink:#1c1c1c;
    --white:#ffffff;
    --page:#ffffff;
    --shadow:rgba(0,0,0,.12);
  }
  *{box-sizing:border-box;margin:0;padding:0}
  html,body{width:1200px;height:2234px;overflow:hidden;background:var(--page)}
  body{font-family:"Poppins",sans-serif;color:var(--ink);position:relative}
  .slide{position:absolute;left:12px;width:1175px;height:660px;overflow:hidden;background:var(--white);box-shadow:0 1px 4px var(--shadow)}
  .slide--cover{top:69px}
  .slide--about{top:759px}
  .slide--why{top:1450px}
  .abs{position:absolute}

  /* cover */
  .cover-photo{right:0;top:0;width:760px;height:660px;background:linear-gradient(90deg,#fff 0%,rgba(236,233,230,.7) 30%,#b9b3ad 60%,#6f625a 100%)}
  .wordmark{font-weight:800;color:var(--navy);line-height:.95;text-transform:uppercase;letter-spacing:1px}
  .cover .wordmark,.slide--cover .wordmark{left:54px;top:68px;font-size:28px;width:150px}
  .cover-title{left:60px;top:196px;font-size:68px;font-weight:800;color:var(--navy);line-height:1;white-space:nowrap}
  .cover-title sup{font-size:40px;vertical-align:28px}
  .cover-sub{left:60px;top:282px;font-size:45px;font-weight:800;color:var(--navy);white-space:nowrap}
  .date-bar{left:58px;top:374px;width:734px;height:39px;display:flex;border:2px solid var(--orange);font-size:19px}
  .date-bar .date{width:245px;background:var(--orange);color:var(--white);display:flex;align-items:center;justify-content:center}
  .date-bar .venue{flex:1;color:var(--orange);display:flex;align-items:center;justify-content:center;background:rgba(255,255,255,.85)}
  .cover-tagline{left:60px;top:446px;font-size:21px;white-space:nowrap}
  .presented{left:60px;top:512px;font-family:"Kalam",cursive;color:var(--orange);font-size:20px}
  .partners{left:58px;top:552px;display:flex;align-items:center;height:52px}
  .partner{font-size:22px;font-weight:700;color:var(--ink);display:flex;align-items:center;gap:8px}
  .partner--second{color:var(--navy);margin-left:28px;padding-left:28px;border-left:1px solid #ddd;height:52px}
  .partner .dot{width:30px;height:30px;border-radius:50%;background:var(--navy)}

  /* about */
  .about-photo{left:0;top:0;width:526px;height:660px;background:linear-gradient(160deg,#c9b79f 0%,#8b6a4e 45%,#4e3a2c 80%,#7b5238 100%)}
  .slide--about .wordmark{left:988px;top:40px;font-size:25px;width:130px;text-align:right}
  .about-heading{left:586px;top:146px;font-size:43px;font-weight:800;line-height:1.12}
  .about-heading .lead{color:var(--orange);display:block}
  .about-heading .name{color:var(--navy);display:block}
  .about-copy{left:586px;top:300px;width:475px;font-size:17.5px;line-height:25px}
  .about-copy p+p{margin-top:12px}
  .about-motto{left:586px;top:528px;font-family:"Kalam",cursive;color:var(--orange);font-size:34px}
  .corner{right:0;bottom:0;width:206px;height:184px}
  .page-num{font-size:14px;color:var(--white);right:36px;bottom:36px}

  /* why */
  .why-bg{left:0;top:0;width:1175px;height:660px;background:radial-gradient(ellipse at 70% 55%,#e6e6e8 0%,#f3f3f4 45%,#fafafa 100%)}
  .why-heading{left:58px;top:60px;font-size:43px;font-weight:800;white-space:nowrap}
  .why-heading .lead{color:var(--orange)}
  .why-heading .name{color:var(--navy)}
  .slide--why .wordmark{left:992px;top:40px;font-size:25px;width:130px;text-align:right;color:rgba(42,53,145,.12)}
  .col{top:188px;width:440px}
  .col--left{left:58px}
  .col--right{left:590px;width:500px}
  .col-icon{width:66px;height:66px;display:block}
  .col-intro{margin-top:28px;font-size:20px;line-height:28px}
  .col-intro strong{color:var(--navy);font-weight:700}
  .checks{list-style:none;margin-top:14px}
  .checks li{position:relative;padding-left:27px;font-size:17.3px;line-height:24px;margin-bottom:15px}
  .checks li::before{content:"✓";position:absolute;left:0;top:0;color:var(--navy);font-size:15px}
  .divider{left:534px;top:229px;width:1px;height:330px;background:#cfcfcf}
  .left-num{left:10px;bottom:20px;font-size:20px;color:var(--ink)}
</style>
</head>
<body>

<section class="slide slide--cover">
  <div class="abs cover-photo" role="img" aria-label="Photo of two young Black men on a city court, one holding a basketball"></div>
  <div class="abs wordmark">Open Every Door</div>
  <h1 class="abs cover-title">OPEN EVERY DOOR <sup>TM</sup></h1>
  <h2 class="abs cover-sub">SPORTS CAREER CONFERENCE</h2>
  <div class="abs date-bar"><span class="date">October 6 – 8,2023</span><span class="venue">Harborpoint Hotel Baltimore, MD</span></div>
  <p class="abs cover-tagline">Career in the Sports Business for HBCU Students and Students of Color</p>
  <p class="abs presented">Presented by:</p>
  <div class="abs partners">
    <span class="partner">Northfield Media</span>
    <span class="partner partner--second"><span class="dot"></span>Courtline Research</span>
  </div>
</section>

<section class="slide slide--about">
  <div class="abs about-photo" role="img" aria-label="Photo of a smiling student in glasses writing in a classroom"></div>
  <div class="abs wordmark">Open Every Door</div>
  <h2 class="abs about-heading"><span class="lead">What is</span><span class="name">Open Every Door?</span></h2>
  <div class="abs about-copy">
    <p>Open Every Door is a three-day event in October 6-8, 2023 that provides HBCU students and college students of color with opportunities to learn more about the business of sports.</p>
    <p>The sports industry is one of the most competitive industries around, yet many don’t truly understand the business of sports the vast amount of opportunities, or what to do to make it happen.</p>
  </div>
  <p class="abs about-motto">We Aim To Change That</p>
  <svg class="abs corner" viewBox="0 0 206 184" aria-hidden="true">
    <path d="M0 184 C110 170 190 110 206 0 L206 184 Z" fill="var(--orange)"/>
    <path d="M14 184 C118 172 194 112 206 14 L206 184 Z" fill="var(--navy)"/>
  </svg>
  <span class="abs page-num">2</span>
</section>

<section class="slide slide--why">
  <div class="abs why-bg" role="img" aria-label="Faded photo of cheerful students gathered together"></div>
  <h2 class="abs why-heading"><span class="lead">Why</span> <span class="name">Open Every Door?</span></h2>
  <div class="abs wordmark">Open Every Door</div>

  <div class="abs col col--left">
    <svg class="col-icon" viewBox="0 0 66 66" fill="none" stroke="var(--navy)" stroke-width="2" aria-hidden="true">
      <circle cx="33" cy="9" r="7"/>
      <path d="M22 40 V26 a11 9 0 0 1 22 0 V40"/>
      <path d="M28 30 v10 M38 30 v10"/>
      <path d="M12 42 l3 6 6 1 -4.5 4 1 6 -5.5 -3 -5.5 3 1 -6 -4.5 -4 6 -1z"/>
      <path d="M33 42 l3 6 6 1 -4.5 4 1 6 -5.5 -3 -5.5 3 1 -6 -4.5 -4 6 -1z"/>
      <path d="M54 42 l3 6 6 1 -4.5 4 1 6 -5.5 -3 -5.5 3 1 -6 -4.5 -4 6 -1z"/>
    </svg>
    <p class="col-intro"><strong>Open Every Door</strong> creates a unique experience for students to learn about the sports business through:</p>
    <ul class="checks">
      <li>Brand &amp; Retailer Keynotes and Case Studies</li>
      <li>Panel discussions with Industry Professionals</li>
      <li>Interactive Workshops</li>
      <li>Networking and More</li>
    </ul>
  </div>

  <div class="abs divider"></div>

  <div class="abs col col--right">
    <svg class="col-icon" viewBox="0 0 66 66" fill="none" stroke="var(--navy)" stroke-width="2" aria-hidden="true">
      <circle cx="33" cy="13" r="11"/><circle cx="13" cy="33" r="11"/><circle cx="53" cy="33" r="11"/><circle cx="33" cy="53" r="11"/>
      <circle cx="33" cy="10" r="3.5"/><path d="M27 19 a6 5 0 0 1 12 0"/>
      <circle cx="13" cy="30" r="3.5"/><path d="M7 39 a6 5 0 0 1 12 0"/>
      <circle cx="53" cy="30" r="3.5"/><path d="M47 39 a6 5 0 0 1 12 0"/>
      <circle cx="33" cy="50" r="3.5"/><path d="M27 59 a6 5 0 0 1 12 0"/>
    </svg>
    <p class="col-intro"><strong>Open Every Door</strong> enables companies to connect with students:</p>
    <ul class="checks">
      <li>Educate them about your company and employment opportunities</li>
      <li>Recruit and build a candidate pipeline</li>
      <li>Teach students about operations, process, strategic planning marketing, sales, finance</li>
    </ul>
  </div>

  <span class="abs left-num">3</span>
  <svg class="abs corner" viewBox="0 0 206 184" aria-hidden="true">
    <path d="M0 184 C110 170 190 110 206 0 L206 184 Z" fill="var(--orange)"/>
    <path d="M14 184 C118 172 194 112 206 14 L206 184 Z" fill="var(--navy)"/>
  </svg>
  <span class="abs page-num">3</span>
</section>

</body>
</html>
```